window design for Pellworth's Butcher Shop

Design an attractive window design (decals) for an old storefront (copy uploaded), which must be very inviting and eye-catching. The old awning (K & R Meats) is being removed and replaced with Pellworth's Butcher Shop (see copy of proposed awning uploaded)

I was inspired by another window decal design (copy uploaded) from Europe. I liked the use of the grey border on the lowest portion of the windows with the lettering in white. I thought the lettering was very eye-catching.

I also liked the use of reds, greys, blacks and whites to match our logo.

I liked the red ribbons incorporated into the grey lower portion of the windows, as well.

There will be a hanging industrial RED dome light installed in each window left and right sides.

WORDING FOR CENTER OF left WINDOW:
-Dry Aged Beef
-Homemade Sausage
WORDING FOR CENTER OF right WINDOW:
-Farm Fresh Poultry
-Wild Game
WORDING FOR LOWEST PORTION OF (left) WINDOW:
-Deli
-Catering
WORDING FOR LOWEST PORTION OF (RIGHT) WINDOW:
-Homestyle Cooking
-Fresh Pasta

The design should not block the view of the inside of the store. I would still like the street traffic to see inside the store (cope uploaded)

Target Market(s)

Middle Income, Italian and Hispanic Clientele

Industry/Entity Type

Shop

Colors
ec1f27
333333
fbfbfb

Requirements
Must have
• use of reds, greys and whites
Nice to have
• I have uploaded a photo from Europe that inspired me
• A more sophisticated design
Should not have
• -Should not block the view into the store
• -Animals are not a must in the design. Ex: cow, pig, chicken, etc.

```html
<!DOCTYPE html>
<html lang="en">
<head>
<meta charset="utf-8">
<title>Pellworth's Storefront – Window Decals</title>
<link rel="stylesheet" href="https://fonts.googleapis.com/css2?family=Lobster&display=swap">
<style>
  :root {
    --red: #ec1f27;
    --charcoal: #333333;
    --charcoal-band: #3a3a3c;
    --glass: #ffffff;
    --paper: #f2f2f2;
    --street: #ececec;
    --ink: #1a1a1a;
    --black: #111111;
    --outline: #4a4a4a;
  }
  * { margin: 0; padding: 0; box-sizing: border-box; }
  html, body { width: 1200px; height: 670px; overflow: hidden; background: var(--paper); }
  .storefront {
    position: relative; width: 1200px; height: 670px;
    background: var(--paper); font-family: "Lobster", cursive; overflow: hidden;
  }
  .project-title {
    position: absolute; left: 35px; top: 20px;
    font-size: 23px; line-height: 29px; color: var(--ink); font-weight: 400;
  }

  /* awning */
  .awning-red { position: absolute; left: 0; top: 89px; width: 1200px; height: 49px; background: var(--red); }
  .awning-dark { position: absolute; left: 0; top: 138px; width: 1200px; height: 48px; background: var(--charcoal-band); }
  .awning-pin-red { position: absolute; left: 0; top: 162px; width: 1200px; height: 3px; background: var(--red); }
  .awning-pin-white { position: absolute; left: 0; top: 173px; width: 1200px; height: 3px; background: var(--glass); }

  /* facade */
  .facade { position: absolute; left: 0; top: 186px; width: 1200px; height: 406px; background: var(--glass); }
  .kickplate { position: absolute; top: 304px; height: 102px; background: var(--charcoal-band); }
  .kickplate--left { left: 0; width: 542px; }
  .kickplate--right { left: 725px; width: 475px; }
  .mullion { position: absolute; top: 0; width: 3px; height: 406px; background: var(--black); }
  .mullion--1 { left: 0; }
  .mullion--2 { left: 363px; }
  .mullion--3 { left: 541px; }
  .mullion--4 { left: 724px; }
  .mullion--5 { left: 912px; }
  .mullion--6 { left: 1197px; }
  .door {
    position: absolute; left: 566px; top: 57px; width: 136px; height: 349px;
    border: 3px solid var(--black); border-bottom: none; background: var(--glass);
  }
  .street { position: absolute; left: 0; top: 592px; width: 1200px; height: 78px; background: var(--street); }

  /* name seals */
  .name-seal {
    position: absolute; border-radius: 50%; background: var(--black);
    display: flex; align-items: center; justify-content: center; text-align: center;
    color: var(--glass); font-family: "Lobster", cursive; font-weight: 400;
  }
  .name-seal--awning {
    left: 567px; top: 71px; width: 134px; height: 134px;
    font-size: 17px; line-height: 21px; box-shadow: 0 0 0 2px var(--glass);
  }
  .name-seal--door { left: 27px; top: 73px; width: 76px; height: 76px; font-size: 10px; line-height: 12px; }

  /* window decals */
  .decal {
    position: absolute; white-space: nowrap; color: var(--red);
    font-family: "Lobster", cursive; font-weight: 400; line-height: 1;
    transform-origin: 0 50%;
    text-shadow:
      1.5px 0 0 var(--glass), -1.5px 0 0 var(--glass), 0 1.5px 0 var(--glass), 0 -1.5px 0 var(--glass),
      2.5px 2.5px 0 var(--outline), -2.5px -2.5px 0 var(--outline), 2.5px -2.5px 0 var(--outline), -2.5px 2.5px 0 var(--outline);
  }
  .decal--beef { left: 58px; top: 289px; font-size: 42px; transform: rotate(-20deg); }
  .decal--sausage { left: 46px; top: 415px; font-size: 42px; transform: rotate(-17deg); }
  .decal--poultry { left: 922px; top: 314px; font-size: 32px; transform: rotate(-16deg); }
  .decal--game { left: 928px; top: 388px; font-size: 40px; transform: rotate(-16deg); }

  .art { position: absolute; background: var(--red); }
  .art--cow { left: 198px; top: 286px; width: 96px; height: 46px; border-radius: 12px; }
  .art--sausage { left: 92px; top: 330px; width: 52px; height: 52px; border-radius: 50%; }
  .art--hen { left: 930px; top: 236px; width: 66px; height: 46px; border-radius: 12px; }
  .art--deer { left: 1104px; top: 312px; width: 66px; height: 76px; border-radius: 12px; }

  /* kickplate lists */
  .service-list {
    position: absolute; list-style: none; color: var(--glass);
    font-family: "Lobster", cursive; font-size: 22px; line-height: 29px;
  }
  .service-list li::before { content: "\2022"; margin-right: 6px; }
  .service-list--left { left: 90px; top: 508px; }
  .service-list--right { left: 934px; top: 508px; }
</style>
</head>
<body>
<main class="storefront">
  <h1 class="project-title">Pellworth's Storefront<br>48-12 Larkfield Ave</h1>

  <div class="awning-red"></div>
  <div class="awning-dark"></div>
  <div class="awning-pin-red"></div>
  <div class="awning-pin-white"></div>

  <section class="facade">
    <div class="kickplate kickplate--left"></div>
    <div class="kickplate kickplate--right"></div>
    <div class="mullion mullion--1"></div>
    <div class="mullion mullion--2"></div>
    <div class="mullion mullion--3"></div>
    <div class="mullion mullion--4"></div>
    <div class="mullion mullion--5"></div>
    <div class="mullion mullion--6"></div>
    <div class="door">
      <div class="name-seal name-seal--door">Pellworth's<br>Butcher Shop</div>
    </div>
  </section>

  <div class="street"></div>

  <div class="name-seal name-seal--awning">Pellworth's<br>Butcher Shop</div>

  <div class="art art--cow" role="img" aria-label="Red silhouette of a cow"></div>
  <div class="art art--sausage" role="img" aria-label="Red coiled sausage illustration"></div>
  <div class="art art--hen" role="img" aria-label="Red silhouette of a rooster"></div>
  <div class="art art--deer" role="img" aria-label="Red silhouette of a leaping deer"></div>

  <p class="decal decal--beef">Dry Aged Beef</p>
  <p class="decal decal--sausage">Homemade Sausage</p>
  <p class="decal decal--poultry">Fresh Farm Poultry</p>
  <p class="decal decal--game">Wild Game</p>

  <ul class="service-list service-list--left">
    <li>Deli</li>
    <li>Fresh Pasta</li>
  </ul>
  <ul class="service-list service-list--right">
    <li>Catering</li>
    <li>Homestyle Cooking</li>
  </ul>
</main>
</body>
</html>
```